Redesign Web Page

I am looking for a great re-design and possibly a banner for TwinFlare.us. The site is for an online dating (self-development, online dating) book. The purpose is to drive book sales.

Target Market(s)

Women 18-55

```html
<!DOCTYPE html>
<html lang="en">
<head>
<meta charset="utf-8">
<title>TwinFlare – online dating made easy</title>
<link href="https://fonts.googleapis.com/css2?family=Montserrat:wght@600;700&family=Lora:wght@400&family=Playfair+Display:wght@700&family=Quicksand:wght@700&family=Yellowtail&display=swap" rel="stylesheet">
<style>
:root{
  --magenta:#b3117f;
  --magenta-dark:#8c0a62;
  --hero-dark:#1e1c1f;
  --hero-mid:#3b3a3d;
  --key-pink:#a0196f;
  --band-grey:#ececec;
  --text:#2a2a2a;
  --footer-grey:#9a9a9a;
  --icon-grey:#b5b5b5;
  --white:#ffffff;
}
*{margin:0;padding:0;box-sizing:border-box}
html,body{width:1200px;height:1181px;overflow:hidden;background:var(--white)}
.page{position:relative;width:1200px;height:1181px;font-family:"Lora",Georgia,serif;color:var(--text)}

.site-header{position:absolute;left:0;top:0;width:1200px;height:110px;
  background:linear-gradient(180deg,var(--magenta) 0%,var(--magenta-dark) 100%)}
.brand{position:absolute;left:40px;top:18px;color:var(--white)}
.brand-name{display:flex;align-items:center;gap:12px;font-family:"Montserrat",sans-serif;font-weight:700;font-size:38px;letter-spacing:1px;line-height:1}
.brand-dot{width:26px;height:26px;border-radius:50%;background:var(--white)}
.brand-tagline{display:block;margin-left:64px;margin-top:6px;font-family:"Lora",serif;font-size:20px;font-weight:400}
.main-nav{position:absolute;right:20px;top:47px;font-family:"Montserrat",sans-serif;font-weight:700;font-size:13px;color:var(--white);text-transform:uppercase;white-space:nowrap}
.main-nav a,.footer-nav a{color:inherit;text-decoration:none}
.sep{margin:0 5px;font-weight:400}

.hero{position:absolute;left:0;top:110px;width:1200px;height:488px;overflow:hidden}
.hero-photo{position:absolute;inset:0;
  background:radial-gradient(ellipse at 68% 38%,var(--key-pink) 0%,rgba(160,25,111,.35) 22%,transparent 45%),
             linear-gradient(160deg,var(--hero-mid) 0%,var(--hero-dark) 60%,#111 100%)}
.hero-title{position:absolute;inset:0;color:var(--white);font-weight:400}
.hero-title span{position:absolute;display:block;line-height:1;white-space:nowrap}
.hero-become{left:38px;top:60px;font-family:"Playfair Display",serif;font-weight:700;font-size:78px}
.hero-queen{left:114px;top:126px;font-family:"Quicksand",sans-serif;font-weight:700;font-size:150px;letter-spacing:1px}
.hero-sub{left:225px;top:283px;font-family:"Quicksand",sans-serif;font-weight:700;font-size:38px}
.hero-script{left:433px;top:330px;font-family:"Yellowtail",cursive;font-weight:400;font-size:66px}

.endorsement{position:absolute;left:0;top:598px;width:1200px;height:199px}
.author-photo{position:absolute;left:95px;top:9px;width:167px;height:165px;
  background:linear-gradient(160deg,#6d5a4e 0%,#c79d86 50%,#4a3d3a 100%)}
.endorsement-quote{position:absolute;left:308px;top:16px;width:880px;font-size:19.5px;line-height:27px}

.posts{position:absolute;left:0;top:797px;width:1200px;height:248px;background:var(--band-grey)}
.post{position:absolute;top:6px;width:555px}
.post-left{left:17px}
.post-right{left:615px}
.post-title{font-family:"Montserrat",sans-serif;font-weight:600;font-size:21px;color:var(--magenta);text-transform:uppercase}
.post-meta{font-size:13px;color:#444}
.post-body{margin-top:22px;font-size:20px;line-height:26.5px}
.read-more{display:block;text-align:right;margin-top:4px;font-family:"Montserrat",sans-serif;font-weight:600;font-size:16px;color:var(--magenta);text-transform:uppercase;text-decoration:none}

.site-footer{position:absolute;left:0;top:1045px;width:1200px;height:136px}
.footer-nav{position:absolute;left:30px;top:50px;font-family:"Montserrat",sans-serif;font-weight:600;font-size:13px;color:var(--footer-grey);text-transform:uppercase;white-space:nowrap}
.social{position:absolute;left:925px;top:28px}
</style>
</head>
<body>
<div class="page">
  <header class="site-header">
    <div class="brand">
      <div class="brand-name"><span class="brand-dot"></span>TwinFlare</div>
      <span class="brand-tagline">online dating made easy</span>
    </div>
    <nav class="main-nav">
      <a href="#">Home</a><span class="sep">|</span><a href="#">About</a><span class="sep">|</span><a href="#">Blog</a><span class="sep">|</span><a href="#">Fan Fair</a><span class="sep">|</span><a href="#">Celeb Endorsements</a><span class="sep">|</span><a href="#">Stories</a><span class="sep">|</span><a href="#">Products</a><span class="sep">|</span><a href="#">Contact</a>
    </nav>
  </header>

  <section class="hero">
    <div class="hero-photo" role="img" aria-label="Close-up of a dark keyboard with pink keys marked with a heart and a woman symbol"></div>
    <h1 class="hero-title">
      <span class="hero-become">Become the</span>
      <span class="hero-queen">QUEEN</span>
      <span class="hero-sub">OF ONLINE DATING</span>
      <span class="hero-script">in a skinny</span>
    </h1>
  </section>

  <section class="endorsement">
    <div class="author-photo" role="img" aria-label="Portrait photo of the endorsing author"></div>
    <p class="endorsement-quote">Helena Marsh, author of four #1 Daily Ledger Best Sellers, "Few things are better than a good sit-down chat with a close girlfriend...especially when she knows what she's talking about. Author Nora Vale becomes your newest close girlfriend and she knows what she's talking about. Like a combination of a relationships therapist and a character out of a Clara Whitby novel, Vale entertainingly delivers some pretty serious goods."</p>
  </section>

  <section class="posts">
    <article class="post post-left">
      <h2 class="post-title">You Are the Spark Rabbit</h2>
      <p class="post-meta">- February 4, 2014 in Energy Tips -</p>
      <p class="post-body">Energy is the root of everything in the Universe. It's both the cause and effect of everything that transpires. In your life your frequency also called your energy or your vibration determines the tangible results which appear in the physical form. Your "reality" is based on your frequency.</p>
      <a class="read-more" href="#">Read More</a>
    </article>
    <article class="post post-right">
      <h2 class="post-title">You Are the Spark Rabbit</h2>
      <p class="post-meta">- February 4, 2014 in Energy Tips -</p>
      <p class="post-body">Energy is the root of everything in the Universe. It's both the cause and effect of everything that transpires. In your life your frequency also called your energy or your vibration determines the tangible results which appear in the physical form. Your "reality" is based on your frequency.</p>
      <a class="read-more" href="#">Read More</a>
    </article>
  </section>

  <footer class="site-footer">
    <nav class="footer-nav">
      <a href="#">Home</a><span class="sep">|</span><a href="#">About</a><span class="sep">|</span><a href="#">Blog</a><span class="sep">|</span><a href="#">Fan Fair</a><span class="sep">|</span><a href="#">Celeb Endorsements</a><span class="sep">|</span><a href="#">Stories</a><span class="sep">|</span><a href="#">Products</a><span class="sep">|</span><a href="#">Contact</a>
    </nav>
    <svg class="social" width="150" height="48" viewBox="0 0 150 48" role="img" aria-label="Social links">
      <circle cx="24" cy="24" r="22" fill="var(--icon-grey)"/>
      <circle cx="72" cy="24" r="22" fill="var(--icon-grey)"/>
      <circle cx="120" cy="24" r="22" fill="var(--icon-grey)"/>
    </svg>
  </footer>
</div>
</body>
</html>
```